Exclusive Wine Label for Australia

We require a new and exclusive wine label for one of our key clients. We are a family winery based in Western Australia with a premium focus. The wine will mainly be sold online so the label will require visual appeal and and a premium focus to fit a price point between $25-$30.

The label will be a revamp of an existing label of ours called Tallow Ridge (bottle image attached) . The only criteria required is to use the name. It can have a totally new look and theme to it. When investigating concepts, look at what the region, Margaret River is know for. It's all about the coastal environment, natural appeal and the relaxed lifestyle that people enjoy when visiting.

The label should be vibrant, colorful and not too serious.

I've also attached one of our labels Tre Colline. This is to give you the structure and layout of how we want the label (please ignore the graphic design and the use of our brand Velmonte) . It's a single wrap label with the dimensions of 88mm tall x 170mm wide.

Our preference is to not use too many expensive finishes such as foils, but embossing and high builds are fine. Velmonte logo is not required and our winery will only be displayed in text where it shows where the product is made.

Target Market(s)

30-50 yrs. No specific gender, but more towards a feminine look

Requirements
Must have
• - Follow the layout of the Tre Colline Label attached.
- Tallow Ridge as the Brand name on label. No reference to Velmonte required
- Fit the price point of $25-30
Nice to have
• It can have a retro look or it can be minimal and modern. I won't put examples up as we are looking for new concepts. Beach themed is the best approach and open to using people on the label as well. Otherwise you can explore making the text as the feature.
Should not have
• Swirls and Waves are overdone. Looking for something more creative.

```html
<!DOCTYPE html>
<html lang="en">
<head>
<meta charset="utf-8">
<title>Tallow Ridge — 2017 Sauvignon Blanc Label</title>
<link rel="stylesheet" href="https://fonts.googleapis.com/css2?family=Caveat+Brush&family=Archivo:wght@400&display=swap">
<style>
  :root {
    --page: #ffffff;
    --wash-light: #d4f1f8;
    --wash-mid: #b6e4f1;
    --wash-deep: #9ed8ea;
    --label: #ffffff;
    --ink: #111111;
    --hat: #b35ad8;
    --fur: #c9986a;
    --shade: #3b3f6b;
  }
  * { box-sizing: border-box; margin: 0; padding: 0; }
  html, body {
    width: 1000px;
    height: 1200px;
    overflow: hidden;
    background: var(--page);
  }
  .canvas {
    position: relative;
    width: 1000px;
    height: 1200px;
    background: var(--page);
  }
  .backdrop-wash {
    position: absolute;
    left: 0;
    top: 90px;
    width: 1000px;
    height: 590px;
  }
  .wine-label {
    position: absolute;
    left: 237px;
    top: 258px;
    width: 526px;
    height: 683px;
    background: var(--label);
    box-shadow: 0 2px 10px rgba(0, 0, 0, 0.28);
  }
  .label-wash {
    position: absolute;
    left: 33px;
    top: 137px;
    width: 420px;
    height: 245px;
  }
  .mascot {
    position: absolute;
    left: 138px;
    top: 67px;
    width: 272px;
    height: 328px;
  }
  .brand-name {
    position: absolute;
    left: 0;
    top: 408px;
    width: 100%;
    text-align: center;
    font-family: "Caveat Brush", cursive;
    font-size: 84px;
    line-height: 80px;
    letter-spacing: 2px;
    text-transform: uppercase;
    color: var(--ink);
  }
  .varietal {
    position: absolute;
    left: 0;
    top: 602px;
    width: 100%;
    text-align: center;
    font-family: "Archivo", Arial, sans-serif;
    font-size: 19px;
    letter-spacing: 0.6px;
    color: var(--ink);
  }
</style>
</head>
<body>
  <main class="canvas">
    <svg class="backdrop-wash" viewBox="0 0 1000 590" role="img" aria-label="Soft light blue watercolour brush stroke behind the label">
      <defs>
        <linearGradient id="washGrad" x1="0" y1="0" x2="1" y2="1">
          <stop offset="0" stop-color="var(--wash-mid)"/>
          <stop offset="0.5" stop-color="var(--wash-light)"/>
          <stop offset="1" stop-color="var(--wash-deep)"/>
        </linearGradient>
      </defs>
      <path d="M150 20 C 380 0, 640 5, 830 30 L 870 95 L 1000 110 L 1000 320 L 860 340 L 620 380 L 400 460 L 190 590 L 150 520 L 60 470 L 0 430 L 0 130 L 110 110 Z" fill="url(#washGrad)"/>
    </svg>

    <section class="wine-label">
      <svg class="label-wash" viewBox="0 0 420 245" role="img" aria-label="Light blue watercolour brush stroke behind the mascot">
        <path d="M10 70 C 120 40, 300 20, 410 40 L 400 170 C 300 200, 160 230, 30 245 L 0 200 Z" fill="var(--wash-mid)"/>
      </svg>

      <svg class="mascot" viewBox="0 0 272 328" role="img" aria-label="Illustrated bulldog wearing a purple bucket hat, heart sunglasses and pink headphones">
        <defs>
          <linearGradient id="mascotGrad" x1="0" y1="0" x2="0" y2="1">
            <stop offset="0" stop-color="var(--hat)"/>
            <stop offset="0.45" stop-color="var(--fur)"/>
            <stop offset="1" stop-color="var(--shade)"/>
          </linearGradient>
        </defs>
        <path d="M70 0 H200 L240 60 L265 200 L220 300 L136 328 L50 300 L5 200 L30 60 Z" fill="url(#mascotGrad)" opacity="0.85"/>
      </svg>

      <h1 class="brand-name">Tallow<br>Ridge</h1>
      <p class="varietal">2017 SAUVIGNON BLANC</p>
    </section>
  </main>
</body>
</html>
```